Maplewood Surgery Brochure Design

Maplewood Surgery (maplewoodsurgery.example)

Is a comprehensive breast care center that focuses on caring for women with breast cancer and other breast pathologies. We need a promotional and marketing brochure, in a tri-fold format, to provide information about our office and describe the services that we offer.

Deliverable

* The brochure should be completed by August 24th
* We will need the necessary files to get the brochure printed (.ai, .indd, etc).

Target Market(s)

Primarily patients of age between 30+ and 70+. The brochure will also be placed in doctor's waiting room

Industry/Entity Type

Marketing

Requirements
Must have
• * Make use of the color scheme as the website (http://maplewoodsurgery.example, http://maplewoodsurgery.example/static/theme-fuchsia.png)
* Incorporate the following graphic elements:
* The company’s logo (provided as an attachment)
* At least one images from the homepage
* Photos of the primary doctor and her staff
* Map to show the office location and phone number
* Enclose a breast cancer self-exam card (http://maplewoodsurgery.example/static/shower-card.jpg)
* A portion of the brochure must be detachable and serve as business cards that can be cut off (see attachment).
Nice to have
• Here is an example of a brochure that we like:

http://designbazaro.example/item/flexible-trifold-brochure/318274?WT.ac=search_item&WT.seg_1=search_item&WT.z_author=mendavik

```html
<!DOCTYPE html>
<html lang="en">
<head>
<meta charset="utf-8">
<title>Maplewood Surgery – Tri-fold Brochure</title>
<link href="https://fonts.googleapis.com/css2?family=Pinyon+Script&family=Open+Sans:wght@400;600&display=swap" rel="stylesheet">
<style>
  :root {
    --pink-soft: #f7d3e4;
    --pink-mid: #efb3d0;
    --pink-deep: #e48cb9;
    --magenta: #b4488a;
    --plum: #8e2a6c;
    --rose-text: #c0609a;
    --ink: #1e1e1e;
    --paper: #ffffff;
    --frame: #e77fb3;
    --card-line: #9a9a9a;
  }
  * { margin: 0; padding: 0; box-sizing: border-box; }
  html, body { width: 1200px; height: 1178px; overflow: hidden; background: var(--paper); }
  .brochure {
    position: relative; width: 1200px; height: 1178px;
    font-family: "Open Sans", Verdana, sans-serif; color: var(--ink);
  }
  .sheet {
    position: absolute; left: 0; top: 0; width: 1200px; height: 925px;
    background:
      radial-gradient(ellipse 420px 360px at 560px 320px, rgba(255,255,255,.85), rgba(255,255,255,0) 70%),
      linear-gradient(180deg, #fdf3f8 0%, #fbe6f0 45%, var(--pink-soft) 75%, var(--pink-mid) 100%);
  }
  .about-heading { position: absolute; left: 64px; top: 98px; font-size: 14px; font-weight: 400; }
  .doctor-photo {
    position: absolute; left: 63px; top: 122px; width: 276px; height: 313px;
    background: radial-gradient(ellipse at 45% 40%, #c9a58c 0%, #6b5a4a 35%, #2f3b52 75%);
    box-shadow: 2px 3px 4px rgba(0,0,0,.35); border: 2px solid #fff;
  }
  .about-text {
    position: absolute; left: 63px; top: 458px; width: 274px;
    font-size: 13px; line-height: 15.4px; text-align: justify;
  }
  .contact-heading { position: absolute; left: 400px; width: 397px; top: 538px; text-align: center; font-size: 17px; font-weight: 400; }
  .map {
    position: absolute; left: 400px; top: 566px; width: 397px; height: 169px;
    background: linear-gradient(135deg, #efece4 0%, #f1efe6 50%, #e9e6dc 100%);
    border: 1px solid #bbb;
  }
  .address {
    position: absolute; left: 400px; width: 397px; top: 764px;
    text-align: center; font-size: 13.5px; line-height: 18.3px;
  }
  .cover-frame {
    position: absolute; left: 817px; top: 27px; width: 361px; height: 872px;
    border: 1.5px solid var(--frame); border-radius: 10px;
    background: linear-gradient(180deg, #fff 0%, #fdf1f6 30%, var(--pink-mid) 60%, var(--pink-deep) 100%);
  }
  .cover-name {
    position: absolute; left: 817px; width: 361px; top: 128px; text-align: center;
    font-size: 34px; color: var(--plum); font-weight: 400; white-space: nowrap;
  }
  .cover-tagline {
    position: absolute; left: 817px; width: 361px; top: 222px; text-align: center;
    font-family: "Pinyon Script", cursive; font-size: 31px; color: var(--rose-text); white-space: nowrap;
  }
  .cover-photo {
    position: absolute; left: 820px; top: 320px; width: 378px; height: 578px;
    background: radial-gradient(ellipse 170px 260px at 55% 50%, #8a5a3e 0%, #6d4430 55%, rgba(231,140,185,0) 100%);
    border-radius: 0 0 10px 10px;
  }
  .card {
    position: absolute; left: 813px; top: 925px; width: 383px; height: 218px;
    border: 1px solid var(--card-line); background: var(--paper);
    transform: rotate(180deg); overflow: hidden;
  }
  .card-name {
    position: absolute; left: 0; width: 100%; top: 36px; text-align: center;
    font-size: 34px; color: var(--plum); white-space: nowrap;
  }
  .card-tagline {
    position: absolute; right: 16px; top: 94px; font-family: "Pinyon Script", cursive;
    font-size: 19px; color: var(--rose-text); white-space: nowrap;
  }
  .card-band {
    position: absolute; left: 0; bottom: 0; width: 100%; height: 78px;
    background: var(--magenta); color: #fff; padding: 8px 16px;
  }
  .card-doctor { font-size: 14px; font-weight: 600; white-space: nowrap; }
  .card-line { font-size: 10.5px; margin-top: 7px; display: flex; gap: 18px; white-space: nowrap; }
  .card-line + .card-line { margin-top: 2px; }
</style>
</head>
<body>
<div class="brochure">
  <div class="sheet"></div>

  <h2 class="about-heading">About Dr. Keswick</h2>
  <div class="doctor-photo" role="img" aria-label="Portrait photo of Dr. Keswick"></div>
  <p class="about-text">To learn more information about Dr. Keswick, the services we offer, important clinical information and all that you need to know concerning insurance and payment, please visit our website: www.maplewoodsurgery.example<br>There, you can download any forms that will need to be printed and completed prior to your visit. There is also a great question-and-answer section which covers many common queries. Additionally, you can email Dr. Keswick directly -- it's easy and confidential.<br>To schedule an appointment, please call us at (555) 014-2052. We look forward to hearing from you soon and participating in your medical care.</p>

  <h2 class="contact-heading">Contact Us</h2>
  <div class="map" role="img" aria-label="Street map showing the office location"></div>
  <p class="address">We are located at the Breast Center inside the<br>Halvorsen Cancer Center<br>On the campus of Brookline Hospital<br>4410 Alderbrook Dr, Suite 100 Westfield, IL 60010<br>Phone: (555) 014-2052 Fax: (555) 014-6683<br>Email us at maplewood.surgery@example.com</p>

  <div class="cover-frame"></div>
  <h1 class="cover-name">Maplewood Surgery</h1>
  <p class="cover-tagline">Comprehensive Breast Care</p>
  <div class="cover-photo" role="img" aria-label="Photo of a serene woman embracing herself, with pale lotus flowers"></div>

  <div class="card">
    <div class="card-name">Maplewood Surgery</div>
    <div class="card-tagline">Comprehensive Breast Care</div>
    <div class="card-band">
      <div class="card-doctor">Dr. Mira T. Keswick, D.O.</div>
      <div class="card-line"><span>phone: (555) 014-2052</span><span>fax: (555) 014-6683</span></div>
      <div class="card-line"><span>maplewood.surgery@example.com</span><span>www.maplewoodsurgery.example</span></div>
    </div>
  </div>
</div>
</body>
</html>
```